Consulting Business Needs a Cover Designed for a New Book

I need a cover for a book that I am going to self-publish that will be called Bold Forge. Ways To Sharpen Your Factory Routines and Quickly Boost Working Capital. The audience is manufacturing companies. I am looking for something that includes something "extreme" in the cover design, such as wing suits, cliff climbing, etc.

Industry/Entity Type

Business

```html
<!DOCTYPE html>
<html lang="en">
<head>
<meta charset="UTF-8">
<title>Bold Forge — Book Cover</title>
<link href="https://fonts.googleapis.com/css2?family=Bebas+Neue&display=swap" rel="stylesheet">
<style>
  :root {
    --stage: #eeeeee;
    --cover-white: #f2f2f2;
    --cover-blue: #3784bf;
    --figure-blue: #84cbe9;
    --subtitle-blue: #3aa6df;
    --title-white: #f4f4f4;
  }
  html, body {
    margin: 0;
    padding: 0;
    width: 1200px;
    height: 904px;
    overflow: hidden;
    background: var(--stage);
  }
  .canvas {
    position: relative;
    width: 1200px;
    height: 904px;
  }
  .book-cover {
    position: absolute;
    left: 320px;
    top: 52px;
    width: 560px;
    height: 800px;
    background: var(--cover-white);
    overflow: hidden;
    box-shadow: 0 6px 24px rgba(0,0,0,0.12);
    font-family: "Bebas Neue", "Arial Narrow", sans-serif;
  }
  .cover-split {
    position: absolute;
    inset: 0;
    width: 100%;
    height: 100%;
  }
  .cover-title {
    position: absolute;
    top: 34px;
    right: 38px;
    margin: 0;
    text-align: right;
    color: var(--title-white);
    font-weight: 400;
    font-size: 150px;
    line-height: 0.86;
    letter-spacing: 1px;
  }
  .cover-title span { display: block; }
  .hero-figure {
    position: absolute;
    left: 200px;
    top: 330px;
    width: 170px;
    height: 120px;
    border-radius: 14px;
    background: var(--figure-blue);
  }
  .cover-subtitle {
    position: absolute;
    right: 38px;
    top: 600px;
    margin: 0;
    text-align: right;
    color: var(--subtitle-blue);
    font-weight: 400;
    font-size: 26px;
    line-height: 1.05;
    letter-spacing: 0.5px;
    white-space: nowrap;
  }
  .cover-subtitle span { display: block; }
</style>
</head>
<body>
<div class="canvas">
  <div class="book-cover">
    <svg class="cover-split" viewBox="0 0 560 800" preserveAspectRatio="none" aria-hidden="true">
      <polygon points="0,0 560,0 560,296 0,800" fill="var(--cover-blue)"/>
    </svg>
    <h1 class="cover-title"><span>Bold</span><span>Forge</span></h1>
    <div class="hero-figure" role="img" aria-label="Light blue silhouette of a wing-suit flyer soaring through the air"></div>
    <p class="cover-subtitle">
      <span>Ways To Sharpen</span>
      <span>Your Factory Routines</span>
      <span>And Quickly Boost Working Capital</span>
    </p>
  </div>
</div>
</body>
</html>
```